Every Drawer Neatly Sorted or EDN Organized needs a business card design. EDN Organized is a professi

We need a business card design that is clean, sharp and conveys a sense of organization. I already have a logo.

Target Market(s)

Families (specifically mothers), small business owners, parents, seniors

Industry/Entity Type

Business

Contact Information for Business Card

My website is www.ednorganized-example.com and my Facebook page is http://www.socialpage-example.com/everydrawerneatlysorted. The phone number is 555-418-2706 and I want to be listed as Miriel O. Dunsford, Owner

Requirements
Must have
• My logo.

```html
<!DOCTYPE html>
<html lang="en">
<head>
<meta charset="utf-8">
<title>EDN Organized – Business Card</title>
<link rel="stylesheet" href="https://fonts.googleapis.com/css2?family=Open+Sans:wght@400&display=swap">
<style>
  :root {
    --page-bg: #ece9e4;
    --card-top: #ffffff;
    --card-bottom: #dadbde;
    --brand-blue: #2d7fc6;
    --ink: #2b2b2b;
    --ink-soft: #333333;
    --card-shadow: rgba(0, 0, 0, 0.22);
  }
  html, body {
    margin: 0;
    padding: 0;
    width: 1200px;
    height: 1200px;
    overflow: hidden;
    background: var(--page-bg);
  }
  .canvas {
    position: relative;
    width: 1200px;
    height: 1200px;
  }
  .business-card {
    position: absolute;
    left: 75px;
    top: 300px;
    width: 1050px;
    height: 600px;
    overflow: hidden;
    background: linear-gradient(to bottom, var(--card-top) 0%, var(--card-top) 20%, var(--card-bottom) 100%);
    box-shadow: 0 6px 14px var(--card-shadow);
    font-family: "Open Sans", Arial, sans-serif;
  }
  .brand-logo {
    position: absolute;
    left: 0;
    right: 0;
    top: 48px;
    height: 76px;
    display: flex;
    justify-content: center;
    align-items: center;
    gap: 22px;
  }
  .brand-mark {
    width: 64px;
    height: 64px;
    background: var(--brand-blue);
    flex: none;
  }
  .brand-name {
    margin: 0;
    font-family: "Open Sans", Arial, sans-serif;
    font-weight: 400;
    font-size: 40px;
    line-height: 1;
    letter-spacing: 4px;
    color: var(--brand-blue);
    white-space: nowrap;
  }
  .holder {
    position: absolute;
    left: 0;
    right: 0;
    top: 308px;
    text-align: center;
  }
  .holder-name {
    margin: 0;
    font-size: 42px;
    line-height: 1.15;
    font-weight: 400;
    color: var(--brand-blue);
  }
  .holder-title {
    margin: 0;
    font-size: 26px;
    line-height: 1.3;
    color: var(--ink-soft);
    letter-spacing: 1px;
  }
  .contact-icons {
    position: absolute;
    top: 445px;
    left: 0;
    right: 0;
    height: 36px;
  }
  .contact-icon {
    position: absolute;
    top: 0;
    width: 36px;
    height: 36px;
    transform: translateX(-50%);
  }
  .icon-social { left: 182px; }
  .icon-phone { left: 525px; }
  .icon-web { left: 846px; }
  .contact-row {
    position: absolute;
    top: 518px;
    left: 0;
    right: 0;
    display: flex;
    justify-content: center;
    align-items: center;
    gap: 22px;
    font-size: 23px;
    letter-spacing: 0.8px;
    color: var(--ink);
    white-space: nowrap;
  }
  .contact-divider { color: var(--ink); }
</style>
</head>
<body>
<div class="canvas">
  <section class="business-card">
    <div class="brand-logo">
      <span class="brand-mark" aria-hidden="true"></span>
      <h1 class="brand-name">Every Drawer Neatly Sorted</h1>
    </div>

    <div class="holder">
      <p class="holder-name">Miriel O. Dunsford</p>
      <p class="holder-title">Owner</p>
    </div>

    <div class="contact-icons">
      <svg class="contact-icon icon-social" viewBox="0 0 36 36" aria-label="Social page">
        <rect x="4" y="4" width="28" height="28" rx="3" fill="var(--brand-blue)"/>
      </svg>
      <svg class="contact-icon icon-phone" viewBox="0 0 36 36" aria-label="Phone">
        <path d="M9 6 C6 6 5 9 5 13 L5 24 C5 28 6 31 9 31 L12 31 C13 31 13 30 13 29 L13 24 C13 23 12 22 11 22 L10 22 L10 15 L11 15 C12 15 13 14 13 13 L13 8 C13 7 13 6 12 6 Z" fill="var(--brand-blue)"/>
        <rect x="15" y="9" width="16" height="22" rx="2" fill="var(--brand-blue)"/>
        <rect x="18" y="12" width="10" height="5" fill="#ffffff"/>
        <g fill="#ffffff">
          <rect x="18" y="19" width="2.5" height="2.5"/><rect x="21.75" y="19" width="2.5" height="2.5"/><rect x="25.5" y="19" width="2.5" height="2.5"/>
          <rect x="18" y="23" width="2.5" height="2.5"/><rect x="21.75" y="23" width="2.5" height="2.5"/><rect x="25.5" y="23" width="2.5" height="2.5"/>
          <rect x="18" y="27" width="2.5" height="2.5"/><rect x="21.75" y="27" width="2.5" height="2.5"/><rect x="25.5" y="27" width="2.5" height="2.5"/>
        </g>
      </svg>
      <svg class="contact-icon icon-web" viewBox="0 0 36 36" aria-label="Website">
        <circle cx="18" cy="18" r="14" fill="var(--brand-blue)"/>
      </svg>
    </div>

    <div class="contact-row">
      <span class="contact-social">everydrawerneatlysorted</span>
      <span class="contact-divider">|</span>
      <span class="contact-phone">555-418-2706</span>
      <span class="contact-divider">|</span>
      <span class="contact-web">www.ednorganized-example.com</span>
    </div>
  </section>
</div>
</body>
</html>
```